Mardi Gras 2013 Design Project

We have a design with elements that we want to retain. However, we need to take what we have and give it a creative BOOST!

Requirements
Must have
• Colors must stay, "KL" logo must stay,
Copy must remain (except - "Requests Your Presence" and small copy in bottom right corner);
Seal must remain, "9th Annual Mardi Gras Ball" frame text can be modified but should resemble;
Gotham font to remain
Nice to have
• Any new Mardi Gras element - like a mask or beads - but can not over shadow copy

```html
<!DOCTYPE html>
<html lang="en">
<head>
<meta charset="utf-8">
<title>9th Annual Mardi Gras Ball</title>
<link rel="stylesheet" href="https://fonts.googleapis.com/css2?family=Montserrat:ital,wght@0,400;0,500;0,800;1,400;1,700;1,800&family=Roboto+Condensed:wght@500&display=swap">
<style>
  :root {
    --sky-top: #c9c9cc;
    --sky-bottom: #f2f2f3;
    --purple: #5a2d7c;
    --purple-deep: #3d1d55;
    --mask: #45215f;
    --lavender: #b08fd6;
    --at-purple: #7a4b9e;
    --green: #4fd44a;
    --gold: #f0c62a;
    --white: #ffffff;
    --sans: "Montserrat", sans-serif;
    --narrow: "Roboto Condensed", sans-serif;
  }
  html, body { margin: 0; padding: 0; overflow: hidden; }
  body { width: 928px; height: 1200px; }
  .poster {
    position: relative;
    width: 928px; height: 1200px;
    overflow: hidden;
    background: linear-gradient(180deg, var(--sky-top), var(--sky-bottom) 40%);
    font-family: var(--sans);
    color: var(--white);
  }
  .backdrop { position: absolute; inset: 0; }
  .mask-art {
    position: absolute;
    left: 47px; top: 60px;
    width: 726px; height: 470px;
    border-radius: 48% 52% 45% 55% / 55% 60% 40% 45%;
    background: radial-gradient(ellipse at 55% 40%, #54296f, var(--mask) 70%);
  }
  .brand-mark {
    position: absolute;
    left: 37px; top: 42px;
    font: 800 112px/1 var(--sans);
    color: var(--gold);
    letter-spacing: -2px;
  }
  .host {
    position: absolute;
    right: 72px; top: 352px;
    text-align: right;
    font: italic 400 23px/1.5 var(--sans);
    color: var(--white);
  }
  .host span { display: block; }
  .host .host-name { margin-right: -28px; }
  .headline { position: absolute; left: 0; top: 0; width: 100%; height: 100%; pointer-events: none; }
  .headline span {
    position: absolute;
    font-family: var(--sans);
    font-style: italic;
    font-weight: 800;
    line-height: 1;
    color: transparent;
    -webkit-text-stroke: 2.5px currentColor;
    white-space: nowrap;
  }
  .word-ordinal { left: 356px; top: 402px; font-size: 190px; -webkit-text-stroke-color: var(--green) !important; filter: drop-shadow(0 0 6px rgba(79,212,74,.35)); }
  .word-annual { left: 505px; top: 540px; font-size: 78px; -webkit-text-stroke-color: var(--gold) !important; }
  .word-mardi { left: 424px; top: 612px; font-size: 118px; -webkit-text-stroke-color: var(--lavender) !important; }
  .word-gras { left: 430px; top: 712px; font-size: 118px; -webkit-text-stroke-color: var(--green) !important; }
  .word-ball { left: 472px; top: 816px; font-size: 118px; -webkit-text-stroke-color: var(--gold) !important; }
  .details {
    position: absolute;
    right: 526px; top: 732px;
    text-align: right;
    white-space: nowrap;
  }
  .details .day, .details .time { font: 500 33px/1.2 var(--narrow); color: var(--white); display: block; }
  .details .date { font: 500 42px/1.15 var(--narrow); color: var(--lavender); display: block; margin: 4px 0 2px; }
  .details .at { font: 500 54px/1 var(--sans); color: var(--at-purple); display: block; margin: 4px 0 0; }
  .venue span { display: block; font: 500 28px/1.1 var(--sans); }
  .venue .venue-type { font-style: italic; font-weight: 400; color: var(--lavender); }
  .rule {
    position: absolute;
    left: 63px; top: 1057px;
    width: 358px; height: 1px;
    background: rgba(255,255,255,.7);
  }
  .address {
    position: absolute;
    right: 526px; top: 1068px;
    text-align: right;
    font: italic 400 18px/1.4 var(--sans);
  }
  .address strong { display: block; font-weight: 700; font-size: 20px; }
  .seal {
    position: absolute;
    left: 429px; top: 984px;
    width: 124px; height: 124px;
    border-radius: 50%;
    background: var(--gold);
    box-shadow: 0 0 0 3px var(--purple-deep), 0 0 0 5px var(--gold);
  }
</style>
</head>
<body>
<main class="poster">
  <svg class="backdrop" width="928" height="1200" viewBox="0 0 928 1200" aria-hidden="true">
    <defs>
      <linearGradient id="night" x1="0" y1="0" x2="0" y2="1">
        <stop offset="0" stop-color="#5e2f82"/>
        <stop offset="1" stop-color="#3a1c52"/>
      </linearGradient>
    </defs>
    <path d="M0 440 C 140 430 230 470 330 430 C 520 360 700 300 928 165 L928 1200 L0 1200 Z" fill="url(#night)"/>
  </svg>

  <div class="mask-art" role="img" aria-label="Masquerade mask on a stick with purple swirls"></div>

  <div class="brand-mark">KL</div>

  <p class="host">
    <span>The Association of</span>
    <span class="host-name">Kingsley Lane Alumni</span>
  </p>

  <h1 class="headline" aria-label="9th Annual Mardi Gras Ball">
    <span class="word-ordinal" style="color:var(--green)">9th</span>
    <span class="word-annual" style="color:var(--gold)">ANNUAL</span>
    <span class="word-mardi" style="color:var(--lavender)">MARDI</span>
    <span class="word-gras" style="color:var(--green)">GRAS</span>
    <span class="word-ball" style="color:var(--gold)">BALL</span>
  </h1>

  <div class="details">
    <span class="day">Saturday</span>
    <span class="date">January 26, 2013</span>
    <span class="time">7pm - 12am</span>
    <span class="at">@</span>
    <div class="venue">
      <span>Peachtree</span>
      <span>Grand</span>
      <span class="venue-type">CONVENTION</span>
      <span class="venue-type">CENTER</span>
    </div>
  </div>

  <div class="rule"></div>

  <p class="address">1450 Exposition Boulevard<strong>ATLANTA, GEORGIA</strong></p>

  <div class="seal" role="img" aria-label="School seal"></div>
</main>
</body>
</html>
```